Gum Creek Critters business card and social media card

I would like 2 designs,

one with my logo that I have (attached file) for the front and then the chatterbook, Snapgallery and wanderguide icons on the back.I would like it to be eye catching.

The second design i would like the designers to come up with.I am looking for a colorful and eye catching but easy to read business card. I am in the center of Australia and would like earthy colors like orange/red, yellow, charcoal, brown, green etc. I would like a blue tongue lizard and a king brown snake in the design for the front. For the back I would like the Chatterbook, Snapgallery and wander guide logos.

Industry/Entity Type

Business

Contact Information for Business Card

Marcus Toller
CEO
GUM CREEK CRITTERS pty ltd
W: 041 907 2286
M: 048 216 0947
E: marcus@gumcreekcritters-example.com.au

Font styles to use
Other font styles liked:
• chiller

Colors
f37122
fbed22
ec1f27
474747
0492cd
acd036

Requirements
Must have
• Business name or my logo (attached file)
• Gum Creek Critters (in a cool font, like "chiller")
• Chatterbook icon
• Snapgallery icon
• Wanderguide icon
Nice to have
• Snake and a blue tongue lizard (either the full animals or just the heads)

```html
<!DOCTYPE html>
<html lang="en">
<head>
<meta charset="utf-8">
<title>Gum Creek Critters – Business Card</title>
<link rel="stylesheet" href="https://fonts.googleapis.com/css2?family=Open+Sans:wght@400;600&family=Gochi+Hand&display=swap">
<style>
  :root {
    --stage: #0f0f0f;
    --red: #ec1f27;
    --red-soft: #ef4a3f;
    --orange: #f37122;
    --yellow: #fbed22;
    --green: #acd036;
    --green-light: #d3e23a;
    --charcoal: #474747;
    --ink: #1e1e1e;
  }
  * { box-sizing: border-box; margin: 0; padding: 0; }
  html, body {
    width: 1200px; height: 1000px; overflow: hidden;
    background: var(--stage);
    font-family: "Open Sans", Arial, sans-serif;
  }
  .stage {
    position: relative; width: 1200px; height: 1000px;
  }
  .card {
    position: absolute; top: 345px;
    width: 520px; height: 310px;
    border-radius: 24px; overflow: hidden;
    box-shadow: 0 18px 40px rgba(0,0,0,.6);
  }
  .card svg.card-bg { position: absolute; inset: 0; width: 100%; height: 100%; }
  .card-front { left: 50px; }
  .card-back { left: 630px; }

  /* front */
  .brand-mark {
    position: absolute; left: 210px; top: 120px;
    display: flex; align-items: center; gap: 12px;
  }
  .brand-mark .dot {
    width: 30px; height: 30px; border-radius: 50%;
    background: var(--orange);
  }
  .brand-mark .brand-name {
    font-weight: 600; font-size: 28px; line-height: 1.05;
    color: var(--red); width: 200px;
  }

  /* back */
  .person { position: absolute; left: 30px; top: 26px; color: var(--ink); }
  .person-name { font-size: 24px; font-weight: 400; }
  .person-role { font-size: 12px; margin-top: -2px; }
  .company {
    position: absolute; left: 30px; top: 100px;
    font-family: "Gochi Hand", "Comic Sans MS", cursive;
    font-size: 26px; color: var(--ink); letter-spacing: .5px;
  }
  .contact {
    position: absolute; left: 30px; top: 160px;
    list-style: none; font-size: 12.5px; line-height: 1.45; color: var(--ink);
  }
  .socials {
    position: absolute; right: 22px; bottom: 20px;
    list-style: none; display: flex; flex-direction: column; gap: 6px; align-items: flex-end;
  }
  .social { display: flex; align-items: center; gap: 8px; }
  .social-label { font-size: 13px; font-weight: 600; color: var(--yellow); }
  .social-dot {
    width: 22px; height: 22px; border-radius: 50%;
    border: 2px solid var(--charcoal);
  }
</style>
</head>
<body>
<main class="stage">

  <section class="card card-front" aria-label="Card front">
    <svg class="card-bg" viewBox="0 0 520 310" aria-hidden="true">
      <defs>
        <linearGradient id="frontRed" x1="0" y1="0" x2="1" y2="1">
          <stop offset="0" stop-color="#ef4a3f"/>
          <stop offset="1" stop-color="#ec1f27"/>
        </linearGradient>
        <linearGradient id="frontGreen" x1="0" y1="1" x2="1" y2="0">
          <stop offset="0" stop-color="#b8d43a"/>
          <stop offset="1" stop-color="#acd036"/>
        </linearGradient>
      </defs>
      <rect width="520" height="310" fill="url(#frontRed)"/>
      <path d="M55 310 C110 140 290 60 520 46 L520 310 Z" fill="#f37122"/>
      <path d="M78 310 C135 155 305 82 520 70 L520 310 Z" fill="url(#frontGreen)"/>
    </svg>
    <svg class="card-bg" viewBox="0 0 520 310" role="img" aria-label="Faint map of Australia behind the logo">
      <defs>
        <radialGradient id="mapGlow" cx=".5" cy=".5" r=".5">
          <stop offset="0" stop-color="#e6e83a" stop-opacity=".85"/>
          <stop offset="1" stop-color="#e6e83a" stop-opacity="0"/>
        </radialGradient>
      </defs>
      <ellipse cx="320" cy="170" rx="170" ry="105" fill="url(#mapGlow)"/>
    </svg>
    <div class="brand-mark">
      <span class="dot"></span>
      <span class="brand-name">Gum Creek Critters</span>
    </div>
  </section>

  <section class="card card-back" aria-label="Card back">
    <svg class="card-bg" viewBox="0 0 520 310" aria-hidden="true">
      <defs>
        <linearGradient id="backGreen" x1="0" y1="1" x2="1" y2="0">
          <stop offset="0" stop-color="#acd036"/>
          <stop offset="1" stop-color="#b8d43a"/>
        </linearGradient>
        <linearGradient id="backRed" x1="0" y1="0" x2="1" y2="1">
          <stop offset="0" stop-color="#ef4a3f"/>
          <stop offset="1" stop-color="#ec1f27"/>
        </linearGradient>
      </defs>
      <rect width="520" height="310" fill="url(#backGreen)"/>
      <path d="M160 310 C320 300 450 220 478 0 L520 0 L520 310 Z" fill="#f37122"/>
      <path d="M180 310 C335 300 462 228 498 0 L520 0 L520 310 Z" fill="url(#backRed)"/>
    </svg>
    <svg class="card-bg" viewBox="0 0 520 310" role="img" aria-label="Faint map of Australia behind the contact details">
      <defs>
        <radialGradient id="mapGlowBack" cx=".5" cy=".5" r=".5">
          <stop offset="0" stop-color="#e6e83a" stop-opacity=".8"/>
          <stop offset="1" stop-color="#e6e83a" stop-opacity="0"/>
        </radialGradient>
      </defs>
      <ellipse cx="250" cy="140" rx="180" ry="110" fill="url(#mapGlowBack)"/>
    </svg>

    <div class="person">
      <p class="person-name">Marcus Toller</p>
      <p class="person-role">CEO</p>
    </div>
    <p class="company">GUM CREEK CRITTERS pty ltd</p>
    <ul class="contact">
      <li>W: 041 907 2286</li>
      <li>M: 048 216 0947</li>
      <li>E: marcus@gumcreekcritters-example.com.au</li>
    </ul>
    <ul class="socials">
      <li class="social"><span class="social-label">Wanderguide</span><span class="social-dot"></span></li>
      <li class="social"><span class="social-label">Chatterbook</span><span class="social-dot"></span></li>
      <li class="social"><span class="social-label">Snapgallery</span><span class="social-dot"></span></li>
    </ul>
  </section>

</main>
</body>
</html>
```